Lumen Kinetics Web Design Project

We need to update our web design for our company. Lumen Kinetics™ is a series of Development (Training) Programs that we deliver both for the General Public as well as Corporate Business.

Much of the content needs a refresh but we are keen to get some thoughts now on design and layout, predominantly front page. Happy to take any comments on the content if you think that is relevant as well.

We might look to move the current video clip and bring a more generic 'inspirational' clip to the front page. A good example of this is www.mindcraftoz.example.au

Our courses have a very similar market to Gerald Whitcombe type courses ... both General Public and Corporate business.

Refer our website www.lumenkinetics.example.com

Target Market(s)

General Public as well as Corporate Business. Courses are designed for all. Gerald Whitcombe would be a good 'feel' for what we do.

Industry/Entity Type

Business

Requirements
Must have
• Must have a 'leading edge' type feel to it.
Must look professional.

```html
<!DOCTYPE html>
<html lang="en">
<head>
<meta charset="utf-8">
<title>Lumen Kinetics</title>
<link href="https://fonts.googleapis.com/css2?family=Open+Sans:ital,wdth,wght@0,75..100,300..700;1,75..100,300..700&family=Arimo:ital,wght@0,400;0,700;1,700&display=swap" rel="stylesheet">
<style>
  :root {
    --brand-blue: #1a75bb;
    --navy: #0f3a5f;
    --navy-bar: #154e7d;
    --orange: #f7941d;
    --sky-top: #c9e6f6;
    --sky-light: #eef7fc;
    --band-grey: #d9dcd6;
    --panel-grey: #e6e7e3;
    --body-grey: #666666;
    --callout-grey: #8a8a8a;
    --white: #ffffff;
  }
  * { box-sizing: border-box; margin: 0; padding: 0; }
  html, body { width: 1200px; height: 1000px; overflow: hidden; }
  body {
    position: relative;
    font-family: "Arimo", Arial, sans-serif;
    background: var(--white);
  }
  .sky {
    position: absolute; left: 0; top: 0; width: 1200px; height: 520px;
    background:
      radial-gradient(ellipse 700px 260px at 600px 330px, rgba(255,255,255,.9) 0%, rgba(255,255,255,0) 70%),
      radial-gradient(ellipse 1000px 420px at 600px 300px, var(--sky-light) 30%, var(--sky-top) 75%, #a9d4ee 100%);
  }
  .band {
    position: absolute; left: 0; top: 520px; width: 1200px; height: 156px;
    background: var(--band-grey);
  }
  .band-edge { position: absolute; left: 0; top: 676px; }

  .brand {
    position: absolute; left: 143px; top: 52px;
    color: var(--brand-blue); font-family: "Open Sans", Arial, sans-serif;
    font-weight: 400; font-size: 35px; line-height: 36px; letter-spacing: .5px;
  }
  .brand sup { font-size: 10px; vertical-align: 18px; }

  .utility-nav {
    position: absolute; right: 120px; top: 31px;
    display: flex; font-weight: 700; font-size: 14px;
  }
  .utility-nav a { color: var(--orange); text-decoration: none; padding: 0 12px; border-left: 1px solid #e5c79c; line-height: 16px; }
  .utility-nav a:first-child { border-left: 0; }
  .utility-nav a:last-child { padding-right: 13px; }

  .main-nav {
    position: absolute; left: 380px; top: 81px; width: 700px; height: 40px;
    background: var(--navy); border-radius: 8px;
    display: flex; justify-content: space-around; align-items: center;
    padding: 0 6px; font-size: 15px; line-height: 16px; color: var(--white);
  }
  .main-nav sup { font-size: 9px; }

  .hero-frame {
    position: absolute; left: 120px; top: 156px; width: 960px; height: 420px;
    background: rgba(240,244,245,.85); border-radius: 8px;
    box-shadow: 0 28px 22px -18px rgba(0,0,0,.28);
  }
  .hero {
    position: absolute; left: 140px; top: 177px; width: 920px; height: 380px;
    background: linear-gradient(180deg, #10375c 0%, #2d6c9c 45%, #5ec8f8 100%);
  }
  .hero-title {
    position: absolute; left: 184px; top: 236px;
    white-space: nowrap;
    font-family: "Open Sans", Arial, sans-serif; font-weight: 300;
    font-stretch: 85%;
    font-size: 44px; line-height: 47px; letter-spacing: -1.5px; color: var(--white);
  }
  .hero-quote {
    position: absolute; left: 185px; top: 399px;
    white-space: nowrap;
    font-family: "Open Sans", Arial, sans-serif; font-style: italic; font-weight: 700;
    font-stretch: 85%;
    font-size: 20px; line-height: 26px; letter-spacing: -.6px; color: var(--navy);
  }
  .hero-cite {
    position: absolute; left: 185px; top: 480px;
    font-family: "Open Sans", Arial, sans-serif; font-weight: 700;
    font-stretch: 85%;
    font-size: 17px; line-height: 24px; letter-spacing: -.5px; color: var(--white);
  }
  .video { position: absolute; left: 540px; top: 220px; width: 480px; height: 292px; }
  .video-still {
    position: absolute; left: 0; top: 0; width: 480px; height: 268px;
    background: linear-gradient(135deg, #4f5a2e 0%, #7c8a4a 35%, #a9a6a0 60%, #5c6a36 100%);
  }
  .video-play {
    position: absolute; left: 201px; top: 121px; width: 78px; height: 48px;
    background: #0b1a26; border-radius: 5px;
  }
  .video-controls { position: absolute; left: 0; top: 268px; }

  .tagline {
    position: absolute; left: 0; top: 618px; width: 1200px; text-align: center;
    font-size: 20px; line-height: 24px; color: var(--navy-bar);
  }
  .tagline sup { font-size: 11px; }

  .intro {
    position: absolute; left: 120px; top: 726px;
    white-space: nowrap;
    font-size: 15px; line-height: 24px; color: var(--body-grey);
  }
  .intro a { color: var(--orange); font-weight: 700; text-decoration: none; }

  .callout {
    position: absolute; left: 780px; top: 726px; width: 300px; height: 100px;
    background: var(--panel-grey); border-radius: 8px;
    display: flex; align-items: center; justify-content: center; text-align: center;
    font-style: italic; font-weight: 700; font-size: 19px; line-height: 22px; color: var(--callout-grey);
  }
  .callout::before {
    content: ""; position: absolute; left: 33px; top: -9px;
    border-left: 10px solid transparent; border-right: 10px solid transparent;
    border-bottom: 9px solid var(--panel-grey);
  }

  .section-bar {
    position: absolute; left: 120px; top: 870px; width: 960px; height: 40px;
    background: var(--navy-bar); border-radius: 8px;
    color: var(--white); font-size: 22px; font-weight: 400; line-height: 38px; text-align: center;
    box-shadow: 0 8px 10px -6px rgba(0,0,0,.2);
  }
  .section-bar sup { font-size: 11px; line-height: 0; }
  .section-intro {
    position: absolute; left: 140px; top: 927px; width: 920px; text-align: center;
    white-space: nowrap;
    font-size: 15px; line-height: 24px; color: var(--body-grey);
  }
  .tabs { position: absolute; left: 124px; top: 988px; }
</style>
</head>
<body>
  <div class="sky"></div>
  <div class="band"></div>
  <svg class="band-edge" width="1200" height="8" viewBox="0 0 1200 8" aria-hidden="true">
    <defs>
      <pattern id="scallop" width="16" height="8" patternUnits="userSpaceOnUse">
        <rect width="16" height="2" fill="#d9dcd6"/>
        <ellipse cx="8" cy="0" rx="9" ry="6" fill="#d9dcd6"/>
      </pattern>
    </defs>
    <rect width="1200" height="8" fill="url(#scallop)"/>
  </svg>

  <div class="brand">lumen<br>kinetics<sup>™</sup></div>

  <nav class="utility-nav">
    <a href="#">Home</a><a href="#">About Us</a><a href="#">Contact Us</a>
  </nav>

  <nav class="main-nav">
    <span>Lumen Kinetics<sup>TM</sup></span>
    <span>Our Programmes</span>
    <span>Events</span>
    <span>Our Products</span>
    <span>Articles &amp; Resources</span>
  </nav>

  <div class="hero-frame"></div>
  <section class="hero"></section>
  <h1 class="hero-title">A new way of<br>thinking to create a<br>new way of being</h1>
  <p class="hero-quote">We can’t solve problems by using the<br>same kind of thinking we used when<br>we created them”</p>
  <p class="hero-cite">Harold Penwick</p>

  <div class="video">
    <div class="video-still" role="img" aria-label="Video still of a presenter speaking outdoors in front of green foliage"></div>
    <div class="video-play">
      <svg width="78" height="48" viewBox="0 0 78 48" aria-hidden="true"><path d="M34 12 L46 24 L34 36 Z" fill="#fff"/></svg>
    </div>
    <svg class="video-controls" width="480" height="24" viewBox="0 0 480 24" aria-hidden="true">
      <defs><linearGradient id="ctrl" x1="0" y1="0" x2="0" y2="1"><stop offset="0" stop-color="#f2f2f2"/><stop offset="1" stop-color="#cfcfcf"/></linearGradient></defs>
      <rect width="480" height="24" fill="url(#ctrl)"/>
      <path d="M14 6 L24 12 L14 18 Z" fill="#333"/>
      <line x1="38" y1="0" x2="38" y2="24" stroke="#aaa"/>
      <rect x="48" y="10" width="300" height="3" fill="#999"/>
      <rect x="48" y="10" width="108" height="3" fill="#666"/>
      <rect x="59" y="6" width="12" height="14" rx="2" fill="#555"/>
      <text x="358" y="16" font-family="Arimo, Arial, sans-serif" font-size="11" fill="#333">0:04 / 2:32</text>
      <line x1="418" y1="0" x2="418" y2="24" stroke="#aaa"/>
      <rect x="428" y="9" width="12" height="8" fill="#444"/>
      <line x1="450" y1="0" x2="450" y2="24" stroke="#aaa"/>
      <path d="M457 10 H460 L464 7 V17 L460 14 H457 Z" fill="#444"/>
      <path d="M466 9 Q469 12 466 15" stroke="#444" fill="none"/>
    </svg>
  </div>

  <p class="tagline">Lumen Kinetics<sup>TM</sup> delivers leading edge workshops, semiars and products in a fun and interactive way</p>

  <p class="intro">Lorem ipsum dolor sit amet, consectetur adipisicing elit, sed do eiusmod tempor incididunt ut<br>labore et dolore magna aliqua. Ut enim ad minim veniam, quis nostrud exercitation ullamco laboris<br>nisi ut aliquip ex ea commodo consequat. Duis aute irure dolor in reprehenderit in voluptate velit<br>esse cillum dolore eu fugiat nulla pariatur ... <a href="#">find out more about us ›</a></p>

  <aside class="callout">If there is one thing you do<br>this year ... make sure it’s<br>Lumen Kinetics™</aside>

  <h2 class="section-bar">Experience Lumen Kinetics<sup>TM</sup> for yourself</h2>
  <p class="section-intro">Lorem ipsum dolor sit amet, consectetur adipisicing elit, sed do eiusmod tempor incididunt ut labore et dolore magna aliqua. Ut enim ad minim<br>veniam, quis nostrud exercitation ullamco laboris nisi ut aliquip ex ea commodo consequat duis aute irure dolor in reprehenderit.</p>

  <svg class="tabs" width="952" height="12" viewBox="0 0 952 12" aria-hidden="true">
    <path fill="#f7941d" d="M0 8 Q0 7 3 7 H64 L70 1 L76 7 H137 Q140 7 140 10 V12 H0 Z"/>
    <path fill="#3d7fa6" d="M162 8 Q162 7 165 7 H226 L232 1 L238 7 H299 Q302 7 302 10 V12 H162 Z"/>
    <path fill="#f7941d" d="M324 8 Q324 7 327 7 H388 L394 1 L400 7 H461 Q464 7 464 10 V12 H324 Z"/>
    <path fill="#3d7fa6" d="M486 8 Q486 7 489 7 H550 L556 1 L562 7 H623 Q626 7 626 10 V12 H486 Z"/>
    <path fill="#f7941d" d="M648 8 Q648 7 651 7 H712 L718 1 L724 7 H785 Q788 7 788 10 V12 H648 Z"/>
    <path fill="#3d7fa6" d="M810 8 Q810 7 813 7 H874 L880 1 L886 7 H947 Q950 7 950 10 V12 H810 Z"/>
  </svg>
</body>
</html>
```